Vorel constructions

We are predominantly a residential home builder based in Melbourne, Victoria Australia. We construct houses, apartments, townhouses, multi-unit developments.

The name of the company is "Vorel Constructions"
My company believes in building unique construction projects mainly residential homes. The target customers are upmarket Melbourne residents/investors.

I want the brand name "Vorel" to be part of the logo. There's no need to put the word construction in the logo at this stage.

I would also like some ideas for a slogan e.g. "Just build it." or "We build quality homes." But I would like something unique and different for a slogan not the same old cliche.

vorelconstructions.example.com.au
e: tmelo@vorelconstructions.example.com.au
M: 0417305862
Address: 8/3 Fenwick Lane Clayton VIC 3168

Director:Mr Dinesh Malarkodiyan

```html
<!DOCTYPE html>
<html lang="en">
<head>
<meta charset="utf-8">
<title>Vorel Constructions – Business Card</title>
<link rel="stylesheet" href="https://fonts.googleapis.com/css2?family=Bitter:wght@700&family=Exo+2:wght@500;600&display=swap">
<style>
  :root {
    --navy: #15143a;
    --cyan: #4df5f0;
    --white: #ffffff;
    --slate: #b1b1c6;
    --ink: #0b0b1a;
    --ink-dim: #0e0d26;
  }
  * { margin: 0; padding: 0; box-sizing: border-box; }
  html, body { width: 1200px; height: 714px; overflow: hidden; background: var(--navy); }
  .card {
    position: relative;
    width: 1200px;
    height: 714px;
    background: var(--navy);
    overflow: hidden;
  }
  .corner-block {
    position: absolute; left: 857px; top: 0;
    width: 343px; height: 122px;
    background: var(--slate);
  }
  .brand-name {
    position: absolute; left: 36px; top: 52px;
    font-family: "Exo 2", sans-serif; font-weight: 600;
    font-size: 90px; line-height: 1;
    color: var(--cyan);
  }
  .tagline {
    position: absolute; left: 282px; top: 106px;
    font-family: "Bitter", serif; font-weight: 700;
    font-size: 31px; line-height: 1;
    color: var(--white);
    letter-spacing: 0.3px;
    white-space: nowrap;
  }
  .header-rule {
    position: absolute; left: 31px; top: 150px;
    width: 635px; height: 5px;
    background: var(--white);
  }
  .director-band {
    position: absolute; left: 0; top: 221px;
    width: 968px; height: 63px;
    background: var(--cyan);
  }
  .director-band p {
    position: absolute; left: 78px; top: 19px;
    font-family: "Bitter", serif; font-weight: 700;
    font-size: 22px; line-height: 1;
    color: var(--white);
  }
  .contact-line {
    position: absolute; left: 31px;
    height: 63px; width: 1169px;
    display: flex; align-items: center;
    padding-left: 7px;
    font-family: "Exo 2", sans-serif; font-weight: 600;
    font-size: 39px; line-height: 1;
    color: var(--ink);
    white-space: nowrap;
    letter-spacing: 1.6px;
  }
  .contact-line.on-white { background: var(--white); }
  .contact-line.on-navy { color: var(--ink-dim); }
  .website { top: 378px; }
  .email { top: 441px; }
  .mobile { top: 507px; }
  .address { top: 570px; }
</style>
</head>
<body>
  <main class="card">
    <div class="corner-block"></div>

    <div class="brand-name">Vorel</div>
    <div class="tagline">CRAFTED AROUND YOU</div>
    <div class="header-rule"></div>

    <div class="director-band">
      <p>Director:Mr Dinesh Malarkodiyan</p>
    </div>

    <div class="contact-line on-white website">Website: vorelconstructions.example.com.au</div>
    <div class="contact-line on-navy email">Email: tmelo@vorelconstructions.example.com.au</div>
    <div class="contact-line on-white mobile">Mobile Contact: 0417305862</div>
    <div class="contact-line on-navy address">Address: 8/3 Fenwick Lane Wexmoor VIC 3999</div>
  </main>
</body>
</html>
```